Report Design Template Needed for Strategy Consulting Co.

I have a small consulting business that does market research, develops marketing strategy, and does business development work (sales, finding partners, preparing for investors) for small and medium-sized companies who can’t afford their own full-time marketing person.

Most of my reports are PowerPoint Decks. There is usually a Title Page, a Table of Contents, an Executive Summary, a Detailed Findings section (with some section breaks, so I need a divider page between sections), and a Recommendations section.

I need a report template/style that is attractive, professional and not too bold such that it takes away from the content, which is what they are paying for.

I have color palette ideas and graphics in the attached brief. Please let me know if you need anything else, or if you need graphic files.

Thank you!!

Target Market(s)

Small business professionals, scientists, business development executives.

Industry/Entity Type

Marketing

Font styles to use
Sans Serif

Requirements
Must have
• Should have the sections listed in the brief. Also, need to be able to import the template complete.
Should not have
• Background must not overtake the text

```html
<!DOCTYPE html>
<html lang="en">
<head>
<meta charset="utf-8">
<title>Meridian Partners – Report Template</title>
<link href="https://fonts.googleapis.com/css2?family=Oswald:wght@400;500&family=Roboto+Condensed:wght@300;400&family=PT+Sans:ital,wght@0,400;1,400;1,700&display=swap" rel="stylesheet">
<style>
  :root{
    --stage:#c6c6c6;
    --teal:#178796;
    --teal-dark:#0e6675;
    --teal-light:#3fc0d0;
    --yellow:#f4a900;
    --olive:#7d8f1f;
    --navy:#1e3956;
    --grey-text:#7a7a7a;
    --bar:#cfcfcf;
    --white:#ffffff;
  }
  *{box-sizing:border-box;margin:0;padding:0}
  html,body{width:1200px;height:900px;overflow:hidden;background:var(--stage)}
  body{position:relative;font-family:"PT Sans",sans-serif}
  .slide{position:absolute;width:371px;height:287px;background:var(--white);overflow:hidden}
  .slide svg.wave{position:absolute;left:0;top:0;width:371px;height:287px}
  .s1{left:27px;top:122px}.s2{left:411px;top:122px}.s3{left:796px;top:122px}
  .s4{left:28px;top:419px}.s5{left:412px;top:422px}.s6{left:796px;top:422px}
  .heading{position:absolute;left:19px;top:22px;right:19px;font-family:"Oswald",sans-serif;font-weight:500;font-size:12px;letter-spacing:.2px;color:var(--teal);border-bottom:1px solid #9a9a9a;padding-bottom:1px;line-height:14px}
  .heading .accent{color:var(--olive)}
  .footer-name{position:absolute;left:6px;bottom:6px;font-family:"Roboto Condensed",sans-serif;font-size:7px;color:var(--white);letter-spacing:-.2px}
  .footer-note{position:absolute;right:9px;bottom:6px;font-size:4.5px;color:var(--white)}
  .bottom-strip{position:absolute;left:0;bottom:0;width:100%;height:5px;background:var(--teal-dark)}
  .photo{position:absolute}
  /* title */
  .s1 .photo{left:0;top:0;width:371px;height:230px;background:linear-gradient(100deg,#7fc7cf 0%,#2b9aa8 40%,#117e8d 100%)}
  .welcome{position:absolute;right:32px;top:84px;text-align:right;font-family:"Oswald",sans-serif;font-weight:500;color:var(--yellow);font-size:16px;line-height:24px}
  .welcome .date{font-family:"Roboto Condensed",sans-serif;font-weight:300;font-size:9.5px;color:var(--white);line-height:12px}
  .brand{position:absolute;font-family:"Roboto Condensed",sans-serif;font-weight:400;color:var(--navy);letter-spacing:-.6px}
  .s1 .brand{right:20px;top:230px;font-size:20px}
  /* toc */
  .toc{position:absolute;left:46px;top:74px;width:277px;height:151px;border:2px solid #bdbdbd;border-radius:6px;background:var(--white);box-shadow:1px 2px 3px rgba(0,0,0,.25);padding:11px 12px 0 11px}
  .toc li{list-style:none;display:flex;align-items:center;height:20px;margin-bottom:6px}
  .toc .num{width:22px;height:19px;background:linear-gradient(#2aa3b2,var(--teal-dark));color:var(--white);font-family:"Roboto Condensed",sans-serif;font-size:13px;text-align:center;line-height:19px;border-radius:2px}
  .toc .item{flex:1;margin-left:6px;height:18px;background:var(--bar);border-radius:3px;font-family:"Roboto Condensed",sans-serif;font-weight:300;font-size:9.5px;color:#555;line-height:18px;padding-left:12px}
  /* summary 1 */
  .s3 .band{position:absolute;left:0;top:72px;width:371px;height:74px;background:var(--teal)}
  .s3 .photo{left:18px;top:61px;width:133px;height:104px;background:linear-gradient(160deg,#cfe7f1,#9fc6d8 60%,#6d8fa5)}
  .band-text{position:absolute;left:163px;top:84px;width:192px;font-style:italic;font-weight:700;font-size:5.6px;line-height:12.8px;color:var(--white);text-align:justify}
  .body-text{position:absolute;font-size:5.6px;line-height:13px;color:var(--grey-text);text-align:justify}
  .s3 .body-text{left:163px;top:155px;width:192px}
  /* summary 2 */
  .s4 .photo{left:19px;top:43px;width:334px;height:78px;background:linear-gradient(90deg,#c9ccd0,#eceef0 50%,#d6d8db)}
  .lead{position:absolute;left:19px;top:139px;width:125px;font-size:5.8px;line-height:9.4px;color:var(--teal);text-transform:uppercase}
  .s4 .body-text{left:151px;top:138px;width:190px;font-size:4.4px;line-height:8.4px;color:#666;text-align:left}
  .s4 .body-text p+p{margin-top:8px}
  /* divider */
  .s5 .photo{left:0;top:0;width:371px;height:282px;background:radial-gradient(circle at 85% 20%,#58d2df 0%,#2fb3c3 35%,#1a6d7c 65%,#15232a 100%)}
  .divider-mark{position:absolute;right:19px;top:240px;display:flex;align-items:center}
  .s5 .brand{position:static;font-size:12px;color:var(--navy)}
  .divider-mark .rule{width:1px;height:33px;background:var(--white);margin:0 8px}
  .section-label{font-family:"Oswald",sans-serif;font-size:10px;color:var(--navy)}
  .section-label .accent{color:var(--yellow)}
  /* closing */
  .s6{background:var(--teal)}
  .thanks{position:absolute;left:24px;top:29px;font-family:"Oswald",sans-serif;font-weight:500;font-size:12px;color:var(--yellow);line-height:15px}
  .thanks small{display:block;font-family:"PT Sans",sans-serif;font-weight:400;font-size:6.5px;color:var(--white);line-height:9px}
  .contacts{position:absolute;left:24px;top:79px;list-style:none}
  .contacts li{display:flex;align-items:center;height:14.5px;font-size:8.8px;color:var(--white)}
  .contacts svg{width:9px;height:9px;margin-right:4px}
  .social{position:absolute;left:24px;top:149px;display:flex;gap:6px}
  .social span{width:14px;height:14px;background:var(--white);border-radius:2px}
  .s6 .brand{right:17px;top:228px;font-size:20px}
</style>
</head>
<body>

<section class="slide s1">
  <div class="photo" role="img" aria-label="Team of professionals seated at a conference table, toned in teal"></div>
  <svg class="wave" viewBox="0 0 371 287" aria-hidden="true">
    <path d="M0 222 Q90 190 210 188 Q300 188 371 198 V287 H0Z" fill="#0e6675"/>
    <path d="M0 232 Q100 198 220 196 Q300 196 371 218 V287 H0Z" fill="#ffffff"/>
    <path d="M40 218 Q160 190 300 196" stroke="#7d8f1f" stroke-width="3" fill="none"/>
  </svg>
  <div class="welcome">WELCOME<br>TO OUR PRESENTATION<div class="date">Birmingham, August 25, 2013</div></div>
  <div class="brand">MeridianPartners</div>
  <div class="bottom-strip"></div>
</section>

<section class="slide s2">
  <h2 class="heading">TABLE OF <span class="accent">CONTENT</span></h2>
  <ol class="toc">
    <li><span class="num">1</span><span class="item">Lorem ipsum dolor sit amet</span></li>
    <li><span class="num">2</span><span class="item">Lorem ipsum dolor sit amet</span></li>
    <li><span class="num">3</span><span class="item">Lorem ipsum dolor sit amet</span></li>
    <li><span class="num">4</span><span class="item">Lorem ipsum dolor sit amet</span></li>
    <li><span class="num">5</span><span class="item">Lorem ipsum dolor sit amet</span></li>
  </ol>
  <svg class="wave" viewBox="0 0 371 287" aria-hidden="true">
    <path d="M0 258 Q180 238 371 244 V287 H0Z" fill="#178796"/>
    <path d="M60 272 Q200 254 340 260" stroke="#cdd49a" stroke-width="2" fill="none"/>
    <path d="M0 276 Q180 260 371 264 V287 H0Z" fill="#178796"/>
  </svg>
  <div class="footer-name">MeridianPartners</div>
  <div class="footer-note">Proprietary and Confidential &nbsp;|&nbsp; 2</div>
</section>

<section class="slide s3">
  <h2 class="heading">EXECUTIVE <span class="accent">SUMMARY</span></h2>
  <div class="band"></div>
  <div class="photo" role="img" aria-label="Woman looking through binoculars against a pale sky"></div>
  <p class="band-text">Lorem ipsum dolor sit amet, consectetur adipisicing elit, sed do eiusmod tempor incididunt ut labore et dolore magna aliqua. Ut enim ad minim veniam, quis nostrud exercitation ullamco laboris nisi ut aliquip ex ea commodo</p>
  <p class="body-text">Lorem ipsum dolor sit amet, consectetur adipisicing elit, sed do eiusmod tempor incididunt ut labore et dolore magna aliqua. Ut enim ad minim veniam, quis nostrud exercitation ullamco laboris nisi ut aliquip ex ea commodo consequat. Duis aute irure dolor in reprehenderit in voluptate velit esse cillum dolore eu fugiat nulla pariatur.</p>
  <svg class="wave" viewBox="0 0 371 287" aria-hidden="true">
    <path d="M0 258 Q180 238 371 244 V287 H0Z" fill="#178796"/>
    <path d="M60 272 Q200 254 340 260" stroke="#cdd49a" stroke-width="2" fill="none"/>
    <path d="M0 276 Q180 260 371 264 V287 H0Z" fill="#178796"/>
  </svg>
  <div class="footer-name">MeridianPartners</div>
  <div class="footer-note">Proprietary and Confidential &nbsp;|&nbsp; 2</div>
</section>

<section class="slide s4">
  <h2 class="heading">EXECUTIVE <span class="accent">SUMMARY</span></h2>
  <div class="photo" role="img" aria-label="Hands working on a laptop and printed charts at a desk"></div>
  <p class="lead">Lorem ipsum dolor sit met consectur adipiscing elit, sed do euismod tempor incididiunt ut labore et delore magna</p>
  <div class="body-text">
    <p>Lorem ipsum dolor sit amet, consectetur adipisicing elit, sed do eiusmod tempor incididunt ut labore et dolore magna aliqua. Ut enim ad minim veniam, quis nostrud exercitation ullamco laboris nisi ut aliquip ex ea commodo consequat. Duis aute irure dolor in reprehenderit in voluptate velit esse cillum dolore eu fugiat nulla pariatur.</p>
    <p>Lorem ipsum dolor sit amet, consectetur adipisicing elit, sed do eiusmod tempor incididunt ut labore et dolore magna aliqua. Ut enim ad minim veniam, quis nostrud exercitation ullamco laboris nisi ut aliquip ex ea commodo consequat. Duis aute irure dolor in reprehenderit in voluptate velit esse cillum dolore eu fugiat nulla pariatur. Excepteur sint occaecat cupidatat non proident, sunt in culpa qui officia deserunt mollit anim id est laborum.</p>
  </div>
  <svg class="wave" viewBox="0 0 371 287" aria-hidden="true">
    <path d="M0 258 Q180 238 371 244 V287 H0Z" fill="#178796"/>
    <path d="M60 272 Q200 254 340 260" stroke="#cdd49a" stroke-width="2" fill="none"/>
    <path d="M0 276 Q180 260 371 264 V287 H0Z" fill="#178796"/>
  </svg>
  <div class="footer-name">MeridianPartners</div>
  <div class="footer-note">Proprietary and Confidential &nbsp;|&nbsp; 2</div>
</section>

<section class="slide s5">
  <div class="photo" role="img" aria-label="Businessman in a suit sketching a glowing light bulb on a teal background"></div>
  <div class="divider-mark">
    <span class="brand">MeridianPartners</span>
    <span class="rule"></span>
    <span class="section-label">SECTION <span class="accent">ONE</span></span>
  </div>
  <div class="bottom-strip"></div>
</section>

<section class="slide s6">
  <h2 class="thanks">THANK YOU<small>For your time</small></h2>
  <ul class="contacts">
    <li><svg viewBox="0 0 10 10"><circle cx="5" cy="5" r="4.4" fill="none" stroke="#fff"/><path d="M2.8 3.6h4.4v3H2.8z M2.8 3.6 5 5.3 7.2 3.6" fill="none" stroke="#fff" stroke-width=".7"/></svg>info@meridianpartners.com</li>
    <li><svg viewBox="0 0 10 10"><circle cx="5" cy="5" r="4.4" fill="none" stroke="#fff"/><ellipse cx="5" cy="5" rx="1.6" ry="3.6" fill="none" stroke="#fff" stroke-width=".6"/><path d="M1.2 5h7.6" stroke="#fff" stroke-width=".6"/></svg>www.meridianpartners.com</li>
    <li><svg viewBox="0 0 10 10"><circle cx="5" cy="5" r="4.4" fill="none" stroke="#fff"/></svg>meridian.partners</li>
    <li><svg viewBox="0 0 10 10"><circle cx="5" cy="5" r="4.4" fill="none" stroke="#fff"/><path d="M3 3.4c.4 2 1.6 3.2 3.6 3.6l.5-.9-1-.6-.5.4c-.6-.3-1.1-.8-1.4-1.4l.4-.5-.6-1z" fill="#fff"/></svg>+49 40 55501234</li>
  </ul>
  <div class="social" aria-label="Social channels"><span></span><span></span><span></span></div>
  <svg class="wave" viewBox="0 0 371 287" aria-hidden="true">
    <path d="M0 212 Q120 172 260 176 Q330 178 371 188 V287 H0Z" fill="#0e6675"/>
    <path d="M0 222 Q140 180 280 184 Q340 186 371 200 V287 H0Z" fill="#ffffff"/>
    <path d="M50 205 Q180 176 300 184" stroke="#7d8f1f" stroke-width="3" fill="none"/>
  </svg>
  <div class="brand">MeridianPartners</div>
  <div class="bottom-strip"></div>
</section>

</body>
</html>
```